Label for natural soft drink / juice

Please see the briefing attached as PDF

Required is a label design that adds a frame for a range of different labels linked to a variety of tastes for a natural, organic, sparkling beverage in a multi-use, environmentally friendly returnable clear glass bottle.
The 2 first tastes are rhubarb and apple
The label will be a paper label sticked at the front side of the bottle.
No glossy or shiny appearance as it does not fit the organic image
No color restrictions in general, but
Blue better than green
Matt better than glossy
Fit of colours on one label essential, so no “crying colour mixture” (great also: complementary contrasts like blue/orange)
Handpainted better than photorealistic
Simple better than overcrowded
Smart, funny intelligent a lot better than same standard as everywhere
For the image consider subtile reminiscence to the fruit or other stuff linked to the fruit (even “across 3 corners”, so a bit far away) as a nice additional asset

Target Market(s)

modern restaurants with high quality food, often with organic and regional products on the menu.

Font styles to use
Serif
Sans Serif
Script

Requirements
Nice to have
• the fruit of the current taste or something linked to the fruit as e.g. reminiscence to well known story or history of the fruit
Should not have
• too many elements on the label. simplicity is key

```html
<!DOCTYPE html>
<html lang="en">
<head>
<meta charset="utf-8">
<title>hartwigs Apple – label series</title>
<link rel="stylesheet" href="https://fonts.googleapis.com/css2?family=Barlow+Condensed:wght@500&family=Oswald:wght@600&display=swap">
<style>
  :root {
    --canvas: #ffffff;
    --cream: #ebebd4;
    --brand-orange: #d2561e;
    --ink: #111111;
    --rust: #c8480f;
    --rust-deep: #a83a0c;
    --amber: #e0930f;
    --amber-deep: #c97a0a;
    --cobalt: #1a56a8;
    --coral: #c9564c;
    --magenta: #c42a78;
    --denim: #1f4f9a;
  }
  * { box-sizing: border-box; margin: 0; padding: 0; }
  html, body {
    width: 1200px;
    height: 1200px;
    overflow: hidden;
    background: var(--canvas);
  }
  .series {
    width: 1200px;
    height: 1200px;
    display: flex;
    align-items: center;
    justify-content: center;
    gap: 50px;
  }
  .label {
    width: 250px;
    height: 305px;
    display: flex;
    flex: none;
  }
  .label__band {
    position: relative;
    width: 100px;
    height: 100%;
    background: var(--cream);
    overflow: hidden;
  }
  .label__brand,
  .label__flavour {
    position: absolute;
    writing-mode: vertical-rl;
    transform: rotate(180deg);
    line-height: 1;
    white-space: nowrap;
  }
  .label__brand {
    left: 2px;
    bottom: 70px;
    font-family: "Barlow Condensed", sans-serif;
    font-weight: 500;
    font-size: 42px;
    color: var(--brand-orange);
  }
  .label__flavour {
    left: 40px;
    bottom: 72px;
    font-family: "Oswald", sans-serif;
    font-weight: 600;
    font-size: 54px;
    letter-spacing: 1px;
    color: var(--ink);
  }
  .label__art {
    flex: 1;
    height: 100%;
  }
  .label__art--rust    { background: linear-gradient(180deg, var(--rust) 0%, var(--rust-deep) 100%); }
  .label__art--amber   { background: linear-gradient(180deg, var(--amber) 0%, var(--amber-deep) 100%); }
  .label__art--cobalt  { background: linear-gradient(180deg, var(--cobalt) 0%, var(--coral) 100%); }
  .label__art--magenta { background: linear-gradient(180deg, var(--magenta) 0%, var(--denim) 100%); }
</style>
</head>
<body>
  <main class="series">
    <section class="label">
      <div class="label__band">
        <span class="label__brand">hartwigs</span>
        <span class="label__flavour">APPLE</span>
      </div>
      <div class="label__art label__art--rust" role="img" aria-label="Geometric pattern of quarter circles and triangles in rust orange and black"></div>
    </section>
    <section class="label">
      <div class="label__band">
        <span class="label__brand">hartwigs</span>
        <span class="label__flavour">APPLE</span>
      </div>
      <div class="label__art label__art--amber" role="img" aria-label="Geometric pattern of half circles and triangles in amber, navy and stone grey"></div>
    </section>
    <section class="label">
      <div class="label__band">
        <span class="label__brand">hartwigs</span>
        <span class="label__flavour">APPLE</span>
      </div>
      <div class="label__art label__art--cobalt" role="img" aria-label="Geometric pattern of half circles and triangles in cobalt blue, coral and navy"></div>
    </section>
    <section class="label">
      <div class="label__band">
        <span class="label__brand">hartwigs</span>
        <span class="label__flavour">APPLE</span>
      </div>
      <div class="label__art label__art--magenta" role="img" aria-label="Geometric pattern of triangles and quarter circles in magenta, blue, black and stone grey"></div>
    </section>
  </main>
</body>
</html>
```